Industrial/Commercial Plumbing Capability Statement

Would like a construction capability statement/Brochure amended to be similar to the attached. -
Have included photos and Notes on the attached
would like project photos to be used
This is a previous capability statement that we would like amended and altered to include, safety, QA and Recent Projects
Please use our company logo
Updates

Need extra days to review

Target Market(s)

Construction work - Industrial

Industry/Entity Type

Plumbing

Requirements
Must have
• Include all items in contents page

Eye Catching Photos relevant to construction industry and relevant to topic on page

```html
<!DOCTYPE html>
<html lang="en">
<head>
<meta charset="utf-8">
<title>Northline Plumbing – Capability Statement</title>
<link href="https://fonts.googleapis.com/css2?family=Montserrat:ital,wght@0,300;0,400;0,600;0,700;0,800;1,400&display=swap" rel="stylesheet">
<style>
:root{
  --navy:#124a72;
  --navy-dark:#0c3654;
  --ink:#3c3c3c;
  --grey-tab:#333a40;
  --line:#9fb3c4;
  --stage:#3b3b3b;
  --white:#ffffff;
}
*{margin:0;padding:0;box-sizing:border-box}
html,body{width:992px;height:1200px;overflow:hidden}
body{background:var(--stage);font-family:'Montserrat',sans-serif;color:var(--ink);position:relative}
.page{position:absolute;width:213px;height:276px;background:var(--white);overflow:hidden}
.col1{left:29px}.col2{left:265px}.col3{left:501px}.col4{left:737px}
.row1{top:31px}.row2{top:320px}.row3{top:609px}.row4{top:898px}
.navy-page{background:var(--navy)}

.heading{position:absolute;left:22px;top:31px;border-left:1px solid var(--navy);padding-left:6px;color:var(--navy);line-height:1}
.heading .light{display:block;font-size:10px;font-weight:300;letter-spacing:.2px}
.heading .bold{display:block;font-size:12.5px;font-weight:800;margin-top:1px}
.navy-page .heading,.on-dark{color:var(--white);border-color:var(--white)}

.footer{position:absolute;left:21px;right:21px;top:260px;display:flex;align-items:center;gap:4px;font-size:3.2px;font-weight:700;color:var(--navy)}
.footer .rule{flex:1;height:.5px;background:var(--navy)}
.footer .num{width:7px;height:7px;border:.6px solid var(--navy);border-radius:50%;display:flex;align-items:center;justify-content:center;font-size:3px}
.on-dark.footer{color:var(--white)}
.on-dark.footer .rule{background:var(--white)}
.on-dark.footer .num{border-color:var(--white)}

.body{position:absolute;left:22px;width:170px;font-size:3.2px;line-height:4.3px}
.body p{margin-bottom:2.6px}
.pull{border-left:1px solid var(--navy);padding-left:5px;color:var(--navy);font-weight:600;font-size:5px;line-height:6px;margin:4px 0 5px}

.wordmark{font-weight:800;color:var(--white);letter-spacing:.2px;display:flex;align-items:center;gap:3px}
.wordmark .dot{width:5px;height:5px;background:currentColor}
.wordmark.navy{color:var(--navy)}

.photo{position:absolute}

/* cover */
.cover-frame{position:absolute;left:6px;top:7px;width:200px;height:269px}
.cover-url{position:absolute;right:12px;top:40px;writing-mode:vertical-rl;transform:rotate(180deg);font-size:4px;color:var(--navy);letter-spacing:.6px}
.cover-title{position:absolute;left:22px;top:205px;border-left:1px solid var(--white);padding-left:6px;color:var(--white);line-height:1}
.cover-title .light{display:block;font-size:12px;font-weight:300}
.cover-title .bold{display:block;font-size:17px;font-weight:800}

/* contents */
.toc{position:absolute;left:29px;right:25px;top:99px;list-style:none;color:var(--white);font-size:4.6px;font-weight:600}
.toc li{display:flex;align-items:flex-end;gap:3px;height:13px}
.toc .leader{flex:1;border-bottom:.5px dotted var(--white);margin-bottom:1px}

/* signatures */
.signers{position:absolute;left:22px;right:22px;top:246px;display:flex;justify-content:space-around;font-size:4.6px;font-weight:600;color:var(--navy)}

/* about box */
.about-box{position:absolute;left:22px;top:139px;width:167px;height:64px;background:var(--navy);display:flex}
.about-box .txt{width:88px;padding:6px 5px;color:var(--white);font-size:2.9px;line-height:3.9px}

/* quote boxes */
.quote-box{position:absolute;background:var(--navy);color:var(--white)}
.quote-box .inner{position:absolute;inset:5px;border:.5px solid rgba(255,255,255,.7)}
.quote-box .mark{position:absolute;font-size:18px;font-weight:800;line-height:1}
.quote-box .text{position:absolute;font-size:3.8px;line-height:5px;font-weight:600}

/* services */
.svc-tab{position:absolute;left:22px;width:167px;height:8px;display:flex;align-items:center}
.svc-tab .label{background:var(--grey-tab);color:var(--white);font-size:5.6px;font-weight:800;padding:0 14px 0 8px;height:8px;line-height:8px;clip-path:polygon(0 0,88% 0,100% 100%,0 100%)}
.svc-tab .tail{flex:1;height:.5px;background:var(--grey-tab);align-self:flex-end}
.svc-icon{position:absolute;left:22px;width:30px;height:40px;background:var(--navy)}
.svc-list{position:absolute;list-style:none;font-size:3.4px;line-height:4.6px;font-weight:700;color:var(--navy)}

/* projects */
.proj{position:absolute;left:22px;width:169px;height:60px}
.proj .pic{position:absolute;left:0;top:11px;width:30px;height:41px}
.proj .card{position:absolute;left:27px;top:4px;width:142px;height:56px;background:var(--navy);color:var(--white);padding:10px 6px 0 25px}
.proj .tab{position:absolute;left:50px;top:0;background:var(--grey-tab);color:var(--white);font-size:5px;font-weight:800;padding:1px 10px 1px 6px;clip-path:polygon(0 0,88% 0,100% 100%,0 100%)}
.proj .name{font-size:4.4px;font-weight:700;line-height:5.2px;margin-bottom:3px}
.proj .meta{display:flex;gap:10px;font-size:3px;line-height:3.8px;font-weight:600;margin-bottom:2px}
.proj .scope{font-size:2.8px;line-height:3.5px}

/* data diagram */
.diagram{position:absolute;left:22px;top:146px;width:170px;height:82px}
.benefit-col{position:absolute;left:14px;top:0;width:48px;height:82px;background:var(--navy)}
.benefit{position:absolute;left:0;width:62px;height:27px;display:flex;align-items:center;gap:5px}
.benefit .ring{width:20px;height:20px;border-radius:50%;background:var(--white);border:2px solid #d9e2ea;flex:none}
.benefit .lbl{color:var(--white);font-size:5px;font-weight:700;line-height:5.6px}
.feature-frame{position:absolute;left:62px;top:8px;width:106px;height:66px;border:.6px solid var(--navy);border-left:none}
.feature{position:absolute;width:40px;text-align:center;font-size:2.8px;font-weight:700;color:var(--ink)}
.feature .dotc{width:12px;height:12px;margin:0 auto 2px;border-radius:50%;background:var(--navy);border:1.5px solid #c8d6e2}

/* team */
.member{position:absolute;left:19px;width:175px;height:44px}
.member .portrait{position:absolute;left:0;top:0;width:44px;height:44px;border-radius:50%;border:1px solid var(--navy);padding:2px}
.member .portrait span{display:block;width:100%;height:100%;border-radius:50%;background:linear-gradient(#d7dde3,#9ea9b3)}
.member .bar{position:absolute;left:49px;top:3px;right:0;height:7px;border-bottom:.5px solid var(--navy)}
.member .name{position:absolute;left:0;top:0;height:7px;background:var(--navy);color:var(--white);font-size:4.6px;font-weight:700;line-height:7px;padding:0 10px 0 5px;clip-path:polygon(0 0,90% 0,100% 100%,0 100%)}
.member .role{position:absolute;right:0;top:2px;font-size:2.9px;font-weight:700;color:var(--navy)}
.member .bio{position:absolute;left:49px;top:13px;right:0;font-size:2.5px;line-height:3.2px}

/* contact */
.contact{position:absolute;left:135px;top:193px;color:var(--white)}
.contact h3{font-size:8px;font-weight:400;border-left:1px solid var(--white);padding-left:5px;line-height:1}
.contact h3 b{font-weight:800}
.contact ul{list-style:none;margin-top:6px;font-size:3.4px;line-height:4.4px}
.contact li{display:flex;gap:3px;margin-bottom:1.5px}
.contact svg{flex:none;margin-top:.5px}
</style>
</head>
<body>

<!-- 01 cover -->
<section class="page col1 row1 cover">
  <div class="cover-frame" role="img" aria-label="City skyline of tall office towers beside a river under a clear blue sky" style="background:linear-gradient(180deg,#8fc0e6 0%,#b9d6ec 45%,#6f8ea6 62%,#3f6d8f 100%)"></div>
  <p class="cover-url">www.northlineplumbing.com.au</p>
  <svg class="photo" style="left:0;top:0" width="213" height="276" viewBox="0 0 213 276" aria-hidden="true">
    <polygon points="0,150 180,225 180,276 0,276" fill="var(--navy)"/>
    <line x1="200" y1="7" x2="200" y2="269" stroke="var(--navy)" stroke-width=".5"/>
  </svg>
  <div class="cover-title"><span class="light">CAPABILITY</span><span class="bold">STATEMENT</span></div>
  <div class="wordmark" style="position:absolute;left:29px;top:252px;font-size:8px"><span class="dot"></span>NORTHLINE</div>
</section>

<!-- 02 contents -->
<section class="page col2 row1 navy-page">
  <div class="heading"><span class="light">TABLE OF</span><span class="bold">CONTENTS</span></div>
  <ul class="toc">
    <li>FROM THE DIRECTORS<span class="leader"></span>03</li>
    <li>ABOUT THE BUSINESS<span class="leader"></span>04</li>
    <li>OUR SERVICES<span class="leader"></span>06</li>
    <li>HEALTH AND SAFETY<span class="leader"></span>07</li>
    <li>QUALITY ASSURANCE<span class="leader"></span>08</li>
    <li>RECENT PROJECTS<span class="leader"></span>09</li>
    <li>NL DATA<span class="leader"></span>10</li>
    <li>MEET THE TEAM<span class="leader"></span>12</li>
  </ul>
  <div class="footer on-dark"><span>www.northlineplumbing.com.au</span><span class="rule"></span><span class="num">02</span></div>
</section>

<!-- 03 directors -->
<section class="page col3 row1">
  <div class="heading"><span class="light">MESSAGE FROM</span><span class="bold">THE DIRECTORS</span></div>
  <div class="body" style="top:66px">
    <p>Our modern approach to plumbing construction means your project benefits from the latest materials, techniques and industry developments. As leaders in high quality construction plumbing, commercial maintenance and retail fit-outs, we stand at the forefront of plumbing in Perth.</p>
    <p>Our innovative and dynamic approach keeps us ahead of our competition and showcases our skill and experience in delivering the right products and installation methods for your projects.</p>
    <div class="pull">We work closely with our Builders on the scope of works, to guarantee that targets are met, and exceeded.</div>
    <p>Northline Plumbing has extensive expertise across many areas, from new shopping centres and hospitals to industrial equipment.</p>
    <p>We constantly strive to exceed the expectations of our customers and have a proven track record with the delivery of large-scale projects, on time and on budget, and firmly believe it is our job to make your project a success and your experience positive.</p>
    <div class="pull">We pride ourselves on having the highest level of quality on-site management in the industry, displaying expert communication, effective collaboration and unmatched problem solving skills. We stand steadfast upon our reputation as problem solvers and innovative and flexible service providers.</div>
    <p>We believe with the proper team, you can avoid costly and unnecessary delays. When you work with us, you know that you are dealing with Perth's most trusted specialists in commercial plumbing.</p>
    <p>We can't wait to start working with you.</p>
  </div>
  <div class="signers"><span>Daniel Reeve</span><span>Marco Bellini</span></div>
  <div class="footer"><span>www.northlineplumbing.com.au</span><span class="rule"></span><span class="num">03</span></div>
</section>

<!-- 04 about -->
<section class="page col4 row1">
  <div class="heading"><span class="light">ABOUT</span><span class="bold">THE BUSINESS</span></div>
  <div class="body" style="top:66px">
    <p>Established in 2004 by Managing Directors Daniel Reeve and Marco Bellini, Northline Plumbing specialises in the commercial sector and has extensive experience in all levels of the industry, from new shopping centres, hotels, high rise developments and hospitals to industrial equipment in both construction and maintenance.</p>
    <p>Our relationships with our suppliers are paramount to the success of our business and we have trading accounts with all major plumbing suppliers in Perth. We maintain working relationships with manufacturers to ensure that we are at the forefront of advancements in the industry.</p>
    <p>We strive for a balance in cost-effective plumbing, whilst keeping the highest standards in the industry. We are relentless in our pursuit of quality and excellence in service. Our approach is built on collaboration, innovation, integrity and accountability, which underpin every interaction at each stage of the work we do.</p>
  </div>
  <div class="about-box">
    <div class="txt">
      <p style="margin-bottom:3px">At Northline Plumbing, we believe our excellent customer relations, passion about the industry and expertise mean we can deliver what we promise. Satisfied customers keep coming back and recommend us to others.</p>
      <p>We know our success depends on the quality of our people. We are committed to attracting and retaining talented employees by providing a strong platform for ongoing career development.</p>
    </div>
    <div role="img" aria-label="Modern multi-storey building with green landscaping" style="flex:1;margin:0;background:linear-gradient(160deg,#cfd8df,#7f8e99 55%,#4f7a4a)"></div>
  </div>
  <div class="body" style="top:213px">
    <p>We proudly employ a highly skilled team of full time staff ranging from qualified tradespeople, apprentices and administration personnel. We are committed to regular, ongoing training and cross-skilling of all our staff and promote a workplace culture that supports career advancement as well as personal growth.</p>
  </div>
  <div class="footer"><span>www.northlineplumbing.com.au</span><span class="rule"></span><span class="num">04</span></div>
</section>

<!-- 05 builder quote -->
<section class="page col1 row2">
  <div class="photo" role="img" aria-label="Construction worker in hard hat and hi-vis vest holding plans, looking at a building under construction" style="left:0;top:0;width:213px;height:189px;background:linear-gradient(120deg,#e9e5df 0%,#d8d2c8 35%,#e58a3c 50%,#c9cdd1 70%,#9aa3aa 100%)"></div>
  <div class="quote-box" style="left:22px;top:154px;width:166px;height:80px">
    <div class="inner"></div>
    <span class="mark" style="left:22px;top:6px">“</span>
    <p class="text" style="left:24px;top:22px;width:122px">As commercial Builders we often have to work on difficult projects that require unique, innovative results. Northline Plumbing are problem solvers and work closely with our team to deliver high quality solution oriented projects. We started working with Northline several years ago and continue to be impressed by their professionalism and attention to detail.</p>
    <span class="mark" style="right:22px;bottom:-4px">”</span>
  </div>
  <div class="wordmark navy" style="position:absolute;right:25px;top:241px;font-size:6.5px"><span class="dot"></span>NORTHLINE</div>
  <div class="footer"><span>www.northlineplumbing.com.au</span><span class="rule"></span><span class="num">05</span></div>
</section>

<!-- 06 services -->
<section class="page col2 row2">
  <div class="heading"><span class="light">OUR</span><span class="bold">SERVICES</span></div>

  <div class="svc-tab" style="top:67px"><span class="label">CONSTRUCTION</span><span class="tail"></span></div>
  <div class="svc-icon" style="top:79px"></div>
  <ul class="svc-list" style="left:70px;top:81px">
    <li>» Airports</li><li>» Apartments / Mixed Use</li><li>» Commercial Fitouts</li><li>» Defence &amp; Government</li><li>» Education</li><li>» Fire Services</li>
  </ul>
  <ul class="svc-list" style="left:131px;top:81px">
    <li>» Hotels</li><li>» Health</li><li>» HVAC – Cooling Towers</li><li>» Multi Storey Office Blocks</li><li>» Retail</li><li>» Sporting / Recreation</li>
  </ul>

  <div class="svc-tab" style="top:131px"><span class="label">MAINTENANCE</span><span class="tail"></span></div>
  <div class="svc-icon" style="top:143px"></div>
  <ul class="svc-list" style="left:70px;top:145px">
    <li>» 24/7 Assistance</li><li>» Backflow Devices</li><li>» Blocked Drains</li><li>» Gas and Water Leaks</li><li>» Hot Water Systems</li><li>» Preventative Maintenance</li>
  </ul>
  <ul class="svc-list" style="left:131px;top:145px">
    <li>» Pump Systems</li><li>» Reactive</li><li>» Roof Leaks</li><li>» Servicing</li><li>» Thermostatic Mixing Valves</li>
  </ul>

  <div class="svc-tab" style="top:195px"><span class="label">SURVEYING</span><span class="tail"></span></div>
  <div class="svc-icon" style="top:207px"></div>
  <ul class="svc-list" style="left:70px;top:209px">
    <li>» Annual Testing</li><li>» Audits</li><li>» Budget Assistance</li><li>» Capital Asset Reports</li><li>» CCTV</li>
  </ul>
  <ul class="svc-list" style="left:131px;top:209px">
    <li>» Design Assistance</li><li>» Pipe Locating</li><li>» Pipework Surveying</li><li>» Preliminary Investigations</li><li>» Water Saving</li>
  </ul>
  <div class="footer"><span>www.northlineplumbing.com.au</span><span class="rule"></span><span class="num">06</span></div>
</section>

<!-- 07 HSE -->
<section class="page col3 row2">
  <div class="heading"><span class="light">HEALTH SAFETY &amp;</span><span class="bold">ENVIRONMENT</span></div>
  <div class="body" style="top:66px">
    <p>The health and safety of all Northline Plumbing employees is essential, and a goal that must not be compromised.</p>
    <p>Northline has a solid reputation for building great business relationships with our clients and this has been helped by our responsible approach to safety on the job.</p>
    <p>We take our employees' and clients' safety seriously and take a proactive approach to health and safety policies by establishing correct guidelines.</p>
    <p>and encourage team involvement to achieve the safest and most efficient outcomes.</p>
  </div>
  <div class="photo" role="img" aria-label="Safety first banner with a yellow hard hat and work gloves resting on timber, cranes in the background" style="left:22px;top:118px;width:167px;height:127px;background:linear-gradient(180deg,#f4c21a 0%,#f4c21a 14%,#9cc4e0 15%,#d7e6f0 55%,#e9a020 72%,#b98a5a 100%)"></div>
  <div class="footer"><span>www.northlineplumbing.com.au</span><span class="rule"></span><span class="num">07</span></div>
</section>

<!-- 08 QA -->
<section class="page col4 row2">
  <div class="photo" role="img" aria-label="Two site workers in hi-vis and hard hats reviewing a tablet together" style="left:0;top:0;width:213px;height:190px;background:linear-gradient(110deg,#ffffff 0%,#f2f2f2 38%,#e3762f 52%,#d56a28 66%,#f3f5c8 82%,#c9d3da 100%)"></div>
  <div class="heading"><span class="light">QUALITY</span><span class="bold">ASSURANCE</span></div>
  <div class="quote-box" style="left:22px;top:166px;width:166px;height:80px">
    <div class="inner"></div>
    <span class="mark" style="left:22px;top:6px">“</span>
    <p class="text" style="left:24px;top:24px;width:120px">Quality assurance is not only something we strive for but something that we are passionate about. Northline Plumbing are market leaders in QA by having the latest software to provide our clients with checkpoints. Photos and signed off by one of our highly skilled tradesman and client representative</p>
    <span class="mark" style="right:22px;bottom:-4px">”</span>
  </div>
  <div class="footer"><span>www.northlineplumbing.com.au</span><span class="rule"></span><span class="num">08</span></div>
</section>

<!-- 09 projects -->
<section class="page col1 row3">
  <div class="heading"><span class="light">RECENT</span><span class="bold">PROJECTS</span></div>

  <article class="proj" style="top:59px">
    <div class="pic" role="img" aria-label="Trench excavation with pipework along a dirt site" style="background:linear-gradient(180deg,#b8c9d6,#a47d52 60%,#6f5a3d)"></div>
    <div class="card">
      <p class="name">Northgate Base Potable Water Infrastructure Upgrade</p>
      <div class="meta"><span>Client:<br>Halden Build</span><span>Hydraulic Value:<br>2.4m</span><span>Completion:<br>May 2021</span></div>
      <p class="scope">Scope: Excavation and installation of over 2km of PE water and fire service. This involved multiple connections and migration of new potable service to existing buildings, sampling and testing all whilst minimising disruption.</p>
    </div>
    <span class="tab">PROJECT:</span>
  </article>

  <article class="proj" style="top:126px">
    <div class="pic" role="img" aria-label="Rail yard with yellow locomotives and industrial sheds" style="background:linear-gradient(180deg,#9fb0bd,#6d747a 55%,#c9a227 70%,#4a4a4a)"></div>
    <div class="card">
      <p class="name">Tarrant Yard – Subdivision</p>
      <div class="meta"><span>Client:<br>Tarrant Rail</span><span>Hydraulic Value:<br>0.8m</span><span>Completion:<br>Jan 2021</span></div>
      <p class="scope">Scope: Relocation of stormwater, water and pumped discharge lines for property subdivision. This included drilling and installing PE water and discharge lines to maintain operation of the rail yard so the client could continue without disruption.</p>
    </div>
    <span class="tab">PROJECT:</span>
  </article>

  <article class="proj" style="top:192px">
    <div class="pic" role="img" aria-label="Modular detention facility building with paved forecourt" style="background:linear-gradient(180deg,#a9c6de,#dfe4e8 55%,#8d9398)"></div>
    <div class="card">
      <p class="name">Redgum Hill Detention Centre</p>
      <div class="meta"><span>Client:<br>Coastal Modular</span><span>Hydraulic Value:<br>1.2m</span><span>Completion:<br>2018</span></div>
      <p class="scope">Scope: 120 bed facility for a government border protection client. Works involved modular construction of facilities in Perth, final connections, fit off and commissioning on site.</p>
    </div>
    <span class="tab">PROJECT:</span>
  </article>
  <div class="footer"><span>www.northlineplumbing.com.au</span><span class="rule"></span><span class="num">09</span></div>
</section>

<!-- 10 data -->
<section class="page col2 row3">
  <div class="heading"><span class="light">NL</span><span class="bold">DATA</span></div>
  <div class="body" style="top:66px">
    <p style="font-size:4.4px;line-height:5.2px;font-weight:700;color:var(--navy)">An Online Asset Management Tool designed for Commercial Property Management</p>
    <p>We understand running and managing large properties and facilities is complex so Northline has developed an online portal through which facilities and property managers can get an overview of the property or properties under their care.</p>
    <p>NL DATA is an online asset management system designed to help cut costs and make the job easier. Quotes, reports, warranties, building plans, maintenance forms, budgeting and compliance documents can all be easily stored and retrieved from the same place.</p>
    <p>NL DATA creates a thorough maintenance history on your property, allowing our team to pre-empt emergency situations and keep your business running smoothly.</p>
    <p>We have a reliable, professional and efficient team guaranteed to deliver above expectations.</p>
  </div>
  <div class="diagram">
    <div class="benefit-col"></div>
    <div class="benefit" style="top:1px"><span class="ring"></span><span class="lbl">SAVE<br>MONEY</span></div>
    <div class="benefit" style="top:28px"><span class="ring"></span><span class="lbl">SAVE<br>TIME</span></div>
    <div class="benefit" style="top:55px"><span class="ring"></span><span class="lbl">GET<br>CONTROL</span></div>
    <div class="feature-frame"></div>
    <div class="feature" style="left:72px;top:0">
      <div class="dotc"></div>MANAGEMENT</div>
    <div class="feature" style="left:112px;top:0"><div class="dotc"></div>PLANS</div>
    <div class="feature" style="left:72px;top:28px"><div class="dotc"></div>SCHEDULING</div>
    <div class="feature" style="left:112px;top:28px"><div class="dotc"></div>AD HOC</div>
    <div class="feature" style="left:72px;top:56px"><div class="dotc"></div>BUDGETING</div>
    <div class="feature" style="left:112px;top:56px"><div class="dotc"></div>WARRANTIES</div>
  </div>
  <div class="footer"><span>www.northlineplumbing.com.au</span><span class="rule"></span><span class="num">10</span></div>
</section>

<!-- 11 data visual -->
<section class="page col3 row3">
  <div class="heading"><span class="light">NL</span><span class="bold">DATA</span></div>
  <div class="photo" role="img" aria-label="Hand holding a tablet surrounded by glowing digital service icons, with the NL DATA name and the line: manage your plumbing services at the push of a button" style="left:22px;top:73px;width:167px;height:129px;background:radial-gradient(circle at 60% 55%,#f3d6e6 0%,#c9d5ec 35%,#8aa3c9 70%,#2b3e5e 100%)"></div>
  <p style="position:absolute;left:22px;top:214px;width:100px;font-size:5.6px;line-height:7px;font-style:italic;color:var(--navy)">An online asset management system designed for commercial property management.</p>
  <div class="wordmark navy" style="position:absolute;right:25px;top:239px;font-size:6.5px"><span class="dot"></span>NORTHLINE</div>
  <div class="footer"><span>www.northlineplumbing.com.au</span><span class="rule"></span><span class="num">11</span></div>
</section>

<!-- 12 team -->
<section class="page col4 row3">
  <div class="heading"><span class="light">MEET</span><span class="bold">THE TEAM</span></div>

  <div class="member" style="top:64px">
    <div class="portrait" role="img" aria-label="Portrait of Daniel Reeve"><span></span></div>
    <div class="bar"><span class="name">DANIEL REEVE</span><span class="role">MANAGING DIRECTOR</span></div>
    <p class="bio">Daniel believes that quality professional relationships are built on the four key values of respect, integrity, teamwork and accountability. He is a licensed plumber and gas fitter with over 20 years of experience in commercial and construction plumbing, working closely with clients, consultants and authorities to deliver projects.</p>
  </div>
  <div class="member" style="top:113px">
    <div class="portrait" role="img" aria-label="Portrait of Marco Bellini"><span></span></div>
    <div class="bar"><span class="name">MARCO BELLINI</span><span class="role">MANAGING DIRECTOR</span></div>
    <p class="bio">Marco is passionate about providing quality service of the highest possible standard and leads the way in implementing industry innovations. He has over 20 years of experience in large-scale commercial plumbing and is known for tailored solutions to challenging projects.</p>
  </div>
  <div class="member" style="top:162px">
    <div class="portrait" role="img" aria-label="Portrait of Sam Whitford"><span></span></div>
    <div class="bar"><span class="name">SAM WHITFORD</span><span class="role">CONSTRUCTION MANAGER</span></div>
    <p class="bio">Sam has been involved in large scale commercial and construction plumbing for over 10 years, working in a variety of settings all over the state. His strong work ethic means he ensures every project runs efficiently and is completed on time and to specification.</p>
  </div>
  <div class="member" style="top:210px">
    <div class="portrait" role="img" aria-label="Portrait of Liam Foster"><span></span></div>
    <div class="bar"><span class="name">LIAM FOSTER</span><span class="role">OPERATIONS MANAGER</span></div>
    <p class="bio">Liam has over fifteen years of project management experience in commercial plumbing and construction. His work history on large scale infrastructure gives him in-depth knowledge of business management and a focus on lasting client relationships.</p>
  </div>
  <div class="footer"><span>www.northlineplumbing.com.au</span><span class="rule"></span><span class="num">12</span></div>
</section>

<!-- 13 full bleed -->
<section class="page col1 row4">
  <div class="photo" role="img" aria-label="Dusk view of a city skyline with tower cranes over a green park, tinted deep blue" style="left:0;top:0;width:213px;height:276px;background:linear-gradient(180deg,#143e6e 0%,#1d4a72 45%,#1f4d5a 62%,#1f5a36 80%,#184a2a 100%)"></div>
  <div class="footer on-dark"><span>www.northlineplumbing.com.au</span><span class="rule"></span><span class="num">13</span></div>
</section>

<!-- 14 back cover -->
<section class="page col2 row4">
  <div class="photo" role="img" aria-label="Smiling tradesman in yellow hard hat and safety glasses using a laptop on a construction site with cranes" style="left:6px;top:7px;width:200px;height:269px;background:linear-gradient(180deg,#a9cde8 0%,#d6e7f3 40%,#f1c232 55%,#3b5f86 72%,#2f4c6b 100%)"></div>
  <svg class="photo" style="left:0;top:0" width="213" height="276" viewBox="0 0 213 276" aria-hidden="true">
    <polygon points="30,276 213,170 213,276" fill="var(--navy)"/>
    <polygon points="206,175 213,171 213,276 206,276" fill="var(--white)"/>
  </svg>
  <div class="contact">
    <h3>CONTACT <b>US</b></h3>
    <ul>
      <li><svg width="3" height="4" viewBox="0 0 6 8"><path d="M3 0a3 3 0 0 1 3 3c0 2-3 5-3 5S0 5 0 3a3 3 0 0 1 3-3z" fill="#fff"/></svg><span>14 Kestrel Way,<br>Belmont WA 6104</span></li>
      <li><svg width="3" height="4" viewBox="0 0 6 8"><path d="M1 0h2l.5 2-1 1a4 4 0 0 0 2 2l1-1 1.5.5V7a1 1 0 0 1-1 1A6 6 0 0 1 0 1a1 1 0 0 1 1-1z" fill="#fff"/></svg><span>(08) 9316 4820</span></li>
      <li><svg width="3" height="4" viewBox="0 0 8 8"><circle cx="4" cy="4" r="3.4" fill="none" stroke="#fff" stroke-width="1"/></svg><span>www.northlineplumbing.com.au</span></li>
    </ul>
  </div>
  <div class="wordmark" style="position:absolute;left:104px;top:254px;font-size:9px"><span class="dot"></span>NORTHLINE</div>
</section>

</body>
</html>
```